Business card design for IT consulting company

Looking for a simple, modern, clean business card design.
Open to reworking our existing logo.

Attached is our current business cards which we do not like.
Ideally double sided with something simple on the back.
Rectangle / Horizonal only.
No rounded edges on the card.
White as the dominate color is preferred.

Target Market(s)

clients, legal, oil & gas, medical, professionals

Industry/Entity Type

IT, tech, consulting

Contact Information for Business Card

Name, Title, email, phone, cell, website

Font styles to use
Sans Serif

Requirements
Must have
• Clean design
Should not have
• loud colors or unusual fonts, etc

```html
<!DOCTYPE html>
<html lang="en">
<head>
<meta charset="utf-8">
<title>Northbyte Solutions – Business Card</title>
<link href="https://fonts.googleapis.com/css2?family=Montserrat:wght@500;700&family=Open+Sans:wght@400;600&display=swap" rel="stylesheet">
<style>
  :root {
    --backdrop: #2b2d31;
    --card-white: #ffffff;
    --card-black: #1a1a1c;
    --navy: #123a8c;
    --ink: #4a4d55;
    --rule-grey: #8a8d94;
    --accent-blue: #17a4e6;
    --icon-red: #e8454a;
    --icon-orange: #f5a21c;
    --icon-navy: #1d3f93;
    --icon-cyan: #1fa6e0;
  }
  * { box-sizing: border-box; margin: 0; padding: 0; }
  html, body { width: 1200px; height: 952px; overflow: hidden; }
  body {
    background: var(--backdrop);
    font-family: "Open Sans", sans-serif;
    position: relative;
  }
  .card {
    position: absolute;
    width: 525px;
    height: 300px;
    border-radius: 0;
    overflow: hidden;
    box-shadow: 0 18px 40px rgba(0,0,0,.45);
  }
  .card--front { left: 45px; top: 326px; background: var(--card-white); }
  .card--back  { left: 630px; top: 326px; background: var(--card-black); }

  /* front */
  .identity { position: absolute; left: 40px; top: 38px; }
  .identity__name {
    font-family: "Montserrat", sans-serif;
    font-weight: 700;
    font-size: 27px;
    letter-spacing: .5px;
    color: var(--navy);
    text-transform: uppercase;
  }
  .identity__title { font-size: 15px; color: var(--ink); margin-top: 2px; }
  .identity__rule { width: 48px; height: 1.5px; background: var(--rule-grey); margin-top: 10px; }

  .contacts { position: absolute; left: 40px; top: 138px; list-style: none; }
  .contacts__item {
    display: flex; align-items: center; gap: 10px;
    font-size: 14px; color: var(--ink); height: 25px;
    white-space: nowrap;
  }
  .contacts__icon {
    width: 18px; height: 18px; border-radius: 3px;
    display: flex; align-items: center; justify-content: center;
    flex: none;
  }
  .contacts__icon--phone  { background: var(--icon-red); }
  .contacts__icon--mobile { background: var(--icon-orange); }
  .contacts__icon--mail   { background: var(--icon-navy); }
  .contacts__icon--web    { background: var(--icon-cyan); }

  .brand { position: absolute; display: flex; align-items: center; gap: 10px; white-space: nowrap; }
  .brand__square { width: 22px; height: 22px; background: var(--accent-blue); border-radius: 3px; }
  .brand__name { font-family: "Montserrat", sans-serif; font-weight: 700; font-size: 30px; }
  .card--front .brand { right: 42px; top: 156px; }
  .card--front .brand__name { color: var(--navy); }

  .accent-line { position: absolute; height: 1.5px; background: var(--accent-blue); }
  .card--front .accent-line--left  { left: 0; width: 270px; top: 262px; }
  .card--front .accent-line--right { right: 0; width: 45px; top: 262px; }

  /* back */
  .card--back .brand { left: 50%; top: 100px; transform: translateX(-50%); }
  .card--back .brand__name { color: #ffffff; }
  .tagline {
    position: absolute; left: 0; right: 0; top: 186px;
    display: flex; align-items: center; gap: 14px;
  }
  .tagline__line { flex: 1; height: 1.5px; background: var(--accent-blue); }
  .tagline__text {
    font-family: "Montserrat", sans-serif; font-weight: 700;
    font-size: 26px; color: #ffffff;
  }
</style>
</head>
<body>

  <section class="card card--front" aria-label="Business card front">
    <div class="identity">
      <h1 class="identity__name">Daniel Reyes</h1>
      <p class="identity__title">IT Consultant</p>
      <div class="identity__rule"></div>
    </div>

    <ul class="contacts">
      <li class="contacts__item">
        <span class="contacts__icon contacts__icon--phone">
          <svg width="11" height="11" viewBox="0 0 24 24"><path fill="#fff" d="M6.6 10.8a15 15 0 0 0 6.6 6.6l2.2-2.2c.3-.3.7-.4 1-.2 1.1.4 2.3.6 3.6.6.6 0 1 .4 1 1V20c0 .6-.4 1-1 1A17 17 0 0 1 3 4c0-.6.4-1 1-1h3.5c.6 0 1 .4 1 1 0 1.3.2 2.5.6 3.6.1.3 0 .7-.2 1z"/></svg>
        </span>
        (800) 555-0147
      </li>
      <li class="contacts__item">
        <span class="contacts__icon contacts__icon--mobile">
          <svg width="9" height="12" viewBox="0 0 12 18"><rect x="1" y="1" width="10" height="16" rx="2" fill="none" stroke="#fff" stroke-width="1.8"/><circle cx="6" cy="14" r="1" fill="#fff"/></svg>
        </span>
        (604) 555-0193
      </li>
      <li class="contacts__item">
        <span class="contacts__icon contacts__icon--mail">
          <svg width="12" height="9" viewBox="0 0 16 12"><rect x="1" y="1" width="14" height="10" fill="none" stroke="#fff" stroke-width="1.6"/><path d="M1 1l7 6 7-6" fill="none" stroke="#fff" stroke-width="1.6"/></svg>
        </span>
        daniel.reyes@northbyte.ca
      </li>
      <li class="contacts__item">
        <span class="contacts__icon contacts__icon--web">
          <svg width="11" height="11" viewBox="0 0 24 24"><path fill="#fff" d="M4 4l16 6-7 2-2 7z"/></svg>
        </span>
        www.northbyte.ca
      </li>
    </ul>

    <div class="brand">
      <span class="brand__square"></span>
      <span class="brand__name">Northbyte</span>
    </div>

    <div class="accent-line accent-line--left"></div>
    <div class="accent-line accent-line--right"></div>
  </section>

  <section class="card card--back" aria-label="Business card back">
    <div class="brand">
      <span class="brand__square"></span>
      <span class="brand__name">Northbyte</span>
    </div>
    <div class="tagline">
      <span class="tagline__line"></span>
      <span class="tagline__text">Solutions</span>
      <span class="tagline__line"></span>
    </div>
  </section>

</body>
</html>
```